Business Card and Simple Logo Desgin

New Zealand based start up company "Brook Advisory LTD" requires business cards and simple logo design.

Card Content.

Brook Advisory LTD

Joanna Pritchard
CA, BMS (Hons)

j.pritchard@brookadvisory.co.nz
PH +64 21 574 160

Target Market(s)

Corporate Business in IT, Finance and accounting.

Industry/Entity Type

Business

```html
<!DOCTYPE html>
<html lang="en">
<head>
<meta charset="utf-8">
<title>Brook Advisory LTD – Business Cards</title>
<link href="https://fonts.googleapis.com/css2?family=Dosis:wght@600&family=Arimo:wght@400;700&display=swap" rel="stylesheet">
<style>
  :root {
    --page: #ffffff;
    --navy-deep: #0b3d78;
    --navy-mid: #1660a8;
    --navy-glow: #2a82cc;
    --amber: #f7ac3a;
    --silver: #dcdfe4;
    --ink: #4a4a4a;
    --name-blue: #1a74c4;
    --muted: #6a6a6a;
    --white: #ffffff;
  }
  * { margin: 0; padding: 0; box-sizing: border-box; }
  html, body { width: 1200px; height: 901px; overflow: hidden; background: var(--page); }
  .sheet { position: relative; width: 1200px; height: 901px; }

  .card {
    position: absolute;
    left: 260px;
    width: 637px;
    height: 364px;
    overflow: hidden;
    box-shadow: 4px 6px 8px rgba(0,0,0,0.35);
  }
  .card--front {
    top: 60px;
    background: radial-gradient(ellipse 70% 90% at 42% 45%, var(--navy-glow) 0%, var(--navy-mid) 38%, var(--navy-deep) 100%);
  }
  .card--back {
    top: 500px;
    background: radial-gradient(ellipse 60% 80% at 75% 50%, var(--navy-glow) 0%, var(--navy-mid) 40%, var(--navy-deep) 100%);
  }

  .brand-mark {
    position: absolute;
    width: 40px; height: 40px;
    background: var(--amber);
  }
  .brand-name {
    position: absolute;
    font-family: 'Dosis', 'Arial Narrow', sans-serif;
    font-weight: 600;
    white-space: nowrap;
    letter-spacing: 0.5px;
  }

  .card--front .brand-mark { left: 50px; top: 223px; }
  .card--front .brand-name { left: 170px; top: 245px; font-size: 38px; color: var(--silver); line-height: 1; }
  .web {
    position: absolute;
    right: 78px; top: 308px;
    font-family: 'Arimo', Arial, sans-serif;
    font-size: 16px;
    color: var(--white);
    letter-spacing: 0.5px;
  }
  .web__domain { color: var(--amber); }

  .back-shape { position: absolute; inset: 0; width: 637px; height: 364px; }

  .card--back .brand-mark { left: 157px; top: 58px; }
  .card--back .brand-name { left: 42px; top: 143px; font-size: 34px; color: var(--ink); line-height: 1; }

  .tab {
    position: absolute;
    left: 0; top: 244px;
    width: 15px; height: 56px;
    background: var(--amber);
    border-radius: 0 8px 8px 0;
  }
  .holder { position: absolute; left: 42px; top: 248px; font-family: 'Arimo', Arial, sans-serif; }
  .holder__name { font-size: 21px; font-weight: 700; color: var(--name-blue); line-height: 1.2; }
  .holder__title { font-size: 16px; color: var(--muted); line-height: 1.3; }

  .contact {
    position: absolute;
    right: 8px; top: 288px;
    font-family: 'Arimo', Arial, sans-serif;
    font-size: 16px;
    color: var(--white);
    text-align: right;
  }
  .contact__row { display: flex; align-items: center; justify-content: flex-end; gap: 8px; line-height: 22px; }
  .contact__icon { width: 14px; height: 14px; flex: none; }
</style>
</head>
<body>
<main class="sheet">

  <section class="card card--front" aria-label="Card front">
    <div class="brand-mark"></div>
    <div class="brand-name">Brook Advisory LTD</div>
    <div class="web">www.<span class="web__domain">brookadvisory</span>.co.nz</div>
  </section>

  <section class="card card--back" aria-label="Card back">
    <svg class="back-shape" viewBox="0 0 637 364" aria-hidden="true">
      <path d="M0 0 H376 Q398 180 272 364 H0 Z" fill="var(--amber)"/>
      <path d="M0 0 H346 Q370 180 245 364 H0 Z" fill="var(--white)"/>
    </svg>

    <div class="brand-mark"></div>
    <div class="brand-name">Brook Advisory LTD</div>

    <div class="tab"></div>
    <div class="holder">
      <div class="holder__name">Joanna Pritchard</div>
      <div class="holder__title">CA, BMS (Hons)</div>
    </div>

    <div class="contact">
      <div class="contact__row">
        <span>+64 21 574 160</span>
        <svg class="contact__icon" viewBox="0 0 14 14" aria-hidden="true">
          <rect x="3.5" y="0.5" width="7" height="13" rx="1.5" fill="var(--amber)"/>
          <rect x="5" y="2.5" width="4" height="6" fill="var(--navy-deep)"/>
        </svg>
      </div>
      <div class="contact__row">
        <span>j.pritchard@brookadvisory.co.nz</span>
        <svg class="contact__icon" viewBox="0 0 14 14" aria-hidden="true">
          <rect x="0.5" y="3" width="13" height="9" fill="var(--amber)"/>
          <path d="M0.5 3 L7 8 L13.5 3" fill="none" stroke="var(--navy-deep)" stroke-width="1"/>
        </svg>
      </div>
    </div>
  </section>

</main>
</body>
</html>
```